Business Card Design Project

Company name will be Tallow Crest (named after my black lab and his fraying muzzle) Business is in the body armor, Security product industry servicing the state, local, and federal law enforcement markets. I want a more formal and serious logo for both business cards and letterhead

```html
<!DOCTYPE html>
<html lang="en">
<head>
<meta charset="utf-8">
<title>Tallow Crest – Business Card</title>
<link rel="stylesheet" href="https://fonts.googleapis.com/css2?family=Montserrat:wght@600&family=Raleway:wght@300;500&family=Source+Sans+3:wght@400&display=swap">
<style>
  :root {
    --card-bg: #ffffff;
    --brand-blue: #2f3f98;
    --mark-dark: #1c1c1c;
    --text-gray: #5a5b5d;
    --text-soft: #6a6b6d;
  }
  html, body {
    margin: 0;
    padding: 0;
    width: 1200px;
    height: 693px;
    overflow: hidden;
    background: var(--card-bg);
  }
  .card {
    position: relative;
    width: 1200px;
    height: 693px;
    background: var(--card-bg);
  }
  .brand {
    position: absolute;
    left: 100px;
    top: 150px;
    display: flex;
    align-items: center;
    gap: 36px;
  }
  .brand-dot {
    width: 270px;
    height: 270px;
    border-radius: 50%;
    background: var(--mark-dark);
    flex: none;
  }
  .brand-name {
    font-family: "Raleway", sans-serif;
    font-weight: 500;
    font-size: 76px;
    letter-spacing: 1px;
    color: var(--brand-blue);
    text-transform: uppercase;
    white-space: nowrap;
  }
  .person {
    position: absolute;
    left: 73px;
    top: 518px;
  }
  .person-name {
    font-family: "Montserrat", sans-serif;
    font-weight: 600;
    font-size: 60px;
    line-height: 1;
    color: var(--text-gray);
    margin: 0;
  }
  .person-title {
    font-family: "Raleway", sans-serif;
    font-weight: 300;
    font-size: 27px;
    color: var(--text-soft);
    margin: 12px 0 0;
  }
  .contact {
    position: absolute;
    right: 51px;
    top: 456px;
    text-align: right;
    font-family: "Source Sans 3", sans-serif;
    font-weight: 400;
    font-size: 31px;
    line-height: 43px;
    color: var(--text-soft);
    font-style: normal;
  }
</style>
</head>
<body>
  <main class="card">
    <div class="brand">
      <div class="brand-dot" aria-hidden="true"></div>
      <div class="brand-name">Tallow Crest</div>
    </div>

    <div class="person">
      <h1 class="person-name">Reid Calloway</h1>
      <p class="person-title">Manufacturers Rep Principal</p>
    </div>

    <address class="contact">
      1470 Harbor View Lane<br>
      Palm Cove, FL 32000<br>
      555-014-2286 cell<br>
      rcalloway.tc@mail.com
    </address>
  </main>
</body>
</html>
```